New solo practice law firm is looking for an elegant, professional, and interactive web design

I need a web design and developer for a new small law firm in Sacramento, California called Dorian Kessly Law, A Professional Corporation. I am a trial lawyer who represents average people facing difficult litigation disputes, including criminal defense as a former prosecutor and civil litigation as a civil litigator. Criminal defense includes domestic violence, battery, assault, drug possession, theft, DUI, etc. Civil litigation includes business disputes, property disputes, employment disputes, family law disputes, and immigration issues. I would like to see web designs that incorporate my logo and use the logo's navy blue and gold colors. I have uploaded the files of my logo to this brief. Please only use the navy blue and gold version. Overall, I want the design to look firm, professional, and elegant.

I plan on having the following pages on my website: (1) Home, (2) Dorian Kessly, (3) Practice Areas, (4) Insights, (5) Contact. I've hand drawn a preliminary sketch concept of what I envision the home page's layout to look like (attached with a text version). I would like your design to keep a similar layout for the homepage and incorporate my logo's colors within it but I am open to creative layout alternatives/ideas. I would like the other pages to have a similar look and feel as the home page. Some of the areas currently in my sketch do not have the full text. You can insert other text for now and I will provide the winner the full text.

In terms of the pictures on the website, I enjoy images of courthouses, columns (example attached but I cannot use this one), and, if possible, images from Sacramento, CA in my background (headshot attached). A plus would be live images that move and also sections of the webpage moving in the viewers view as they scroll down on the page. Also, it would be great to have my logo act as the tab for the website. I can provide other versions of the logo if needed.

I look forward to seeing your Wordpress designs!

People needing legal representation.

Law

Coded - Design and coding required

5+ page

Serif

• Incorporate my logo and my logo's colors.
• Live pictures and images appearing as viewers scroll on page.

```html
<!DOCTYPE html>
<html lang="en">
<head>
<meta charset="utf-8">
<title>Dorian Kessly Law</title>
<link href="https://fonts.googleapis.com/css2?family=Lora:wght@400;600;700&family=Inter:wght@400;500&family=Montserrat:wght@500;600;700&display=swap" rel="stylesheet">
<style>
:root{
  --navy:#15223f;
  --navy-deep:#0f1a33;
  --gold:#ab9566;
  --gold-dark:#8f7a4f;
  --gold-text:#b39a62;
  --ink:#1b2746;
  --body:#5d6170;
  --field:#f1f1f2;
  --field-line:#cfcfd3;
  --paper:#f7f7f8;
}
*{margin:0;padding:0;box-sizing:border-box}
html,body{width:1200px;height:2414px;overflow:hidden}
body{position:relative;background:#fff;font-family:"Inter",Helvetica,Arial,sans-serif;color:var(--body)}
.abs{position:absolute}

/* Hero */
.hero{left:0;top:0;width:1200px;height:600px;
  background:linear-gradient(180deg,#1a2540 0%,#2a2c35 28%,#3b3834 55%,#1b2438 78%,#241f1c 100%)}
.top-address{right:695px;top:22px;text-align:right;color:#fff;font-size:15px;line-height:18px}
.top-brand{left:500px;top:30px;width:200px;text-align:center;color:var(--gold-text);font-family:"Lora",Georgia,serif;font-size:15px;font-weight:600;letter-spacing:.5px}
.top-brand small{display:block;font-size:8px;letter-spacing:1.5px;margin-top:4px;font-weight:400}
.top-contact{left:707px;top:22px;color:#fff;font-size:15px;line-height:19px}
.top-contact .lang{font-size:12px;color:var(--gold-text)}
.top-contact svg{vertical-align:-2px}
.nav{left:203px;top:110px;width:794px;height:60px;background:var(--gold);display:flex;align-items:center}
.nav-mark{width:84px;height:60px;background:var(--gold-dark);display:flex;align-items:center;justify-content:center}
.nav-mark span{width:30px;height:30px;border:2px solid #d8c9a4}
.nav ul{list-style:none;display:flex;gap:0;margin-left:22px}
.nav li{font-family:"Inter",sans-serif;font-weight:500;font-size:13.5px;letter-spacing:1px;color:var(--navy);margin-right:34px}
.hero-name{left:300px;top:300px;width:600px;text-align:center;font-family:"Lora",Georgia,serif;font-weight:600;font-size:56px;color:#c9ad72;letter-spacing:1px}

/* Intro */
.intro{left:0;top:600px;width:1200px;height:508px;background:linear-gradient(180deg,#f2f2f3,#fbfbfb 60%,#f4f4f5)}
.h-serif{font-family:"Lora",Georgia,serif;font-weight:400;color:var(--ink)}
.h-serif b{font-weight:600;color:var(--gold-text)}
.intro h1{left:0;top:62px;width:1200px;text-align:center;font-size:45px}
.intro p{left:245px;top:132px;width:710px;text-align:center;font-size:13.5px;line-height:20px}
.card{top:233px;width:228px;height:182px;display:flex;align-items:center;justify-content:center;font-family:"Montserrat",sans-serif;font-weight:600;font-size:12.5px;color:#fff}
.card.c1{left:124px;background:linear-gradient(160deg,#3b3129,#6b4a2a 55%,#a8672e)}
.card.c2{left:365px;background:linear-gradient(160deg,#2a2a2e,#4a3f36 55%,#8b7563)}
.card.c3{left:609px;background:linear-gradient(160deg,#3e5a5c,#6b7a55 55%,#8a8a52)}
.card.c4{left:849px;background:linear-gradient(160deg,#8a8170,#5f5b4c 55%,#4a4a40)}

/* About */
.about{left:0;top:1108px;width:1200px;height:511px;background:linear-gradient(100deg,#f4f4f5,#ececee 70%,#f3f3f4)}
.about h2{left:189px;top:92px;font-size:45px;line-height:49px}
.about p{left:190px;top:212px;width:450px;font-size:13.5px;line-height:20.3px}
.btn-outline{left:190px;top:388px;width:171px;height:44px;border:1px solid var(--gold);display:flex;align-items:center;justify-content:center;font-family:"Montserrat",sans-serif;font-weight:600;font-size:14px;letter-spacing:2px;color:var(--gold-text);background:transparent}
.portrait{left:695px;top:22px;width:280px;height:489px;background:linear-gradient(180deg,#d9d9db 0%,#2a2d36 45%,#16181e 100%);border-radius:120px 120px 0 0}

/* Consultation */
.consult{left:0;top:1619px;width:1200px;height:476px;background:linear-gradient(180deg,#fff,#f6f6f7 60%,#efeff1)}
.consult h3{left:120px;top:82px;font-family:"Lora",Georgia,serif;font-weight:700;font-size:31px;color:var(--ink)}
.field{left:121px;width:468px;height:38px;background:var(--field);border:1px solid var(--field-line);font-size:12.5px;color:#333;padding:12px 12px}
.submit{left:120px;top:386px;width:148px;height:36px;background:var(--gold);color:#fff;font-family:"Montserrat",sans-serif;font-weight:700;font-size:14px;display:flex;align-items:center;justify-content:center}
.consult h2{left:650px;top:84px;width:480px;font-size:45px;line-height:49px}
.consult p{left:650px;top:260px;width:410px;font-size:13.5px;line-height:20.3px}

/* Footer */
.footer{left:0;top:2095px;width:1200px;height:234px;background:var(--navy)}
.foot-brand{left:130px;top:140px;width:240px;text-align:center;font-family:"Lora",Georgia,serif;font-size:15px;letter-spacing:2px;color:var(--gold-text)}
.foot-brand small{display:block;font-size:8px;letter-spacing:1.5px;margin-top:4px}
.foot-col{top:42px;color:#fff;font-size:14px;line-height:23.3px}
.foot-col h4{font-family:"Lora",Georgia,serif;font-weight:600;font-size:21px;color:var(--gold-text);margin-bottom:10px;line-height:28px}
.social{display:flex;gap:14px;margin-top:4px}
.social span{width:12px;height:12px;border-radius:50%;background:#fff}
.legal{left:0;top:2329px;width:1200px;height:85px;background:var(--gold);color:#fff;text-align:center;padding:15px 140px 0}
.legal p{font-size:11.5px;line-height:17px}
.legal small{display:block;font-family:"Lora",Georgia,serif;font-size:9px;margin-top:6px}
</style>
</head>
<body>

<section class="abs hero" role="img" aria-label="Aerial evening photograph of Sacramento riverfront with the gold bridge"></section>
<div class="abs top-address">2718 Larkspur Row<br>Suite # 305<br>Fairhaven, CA 95731</div>
<div class="abs top-brand">Dorian Kessly Law<small>A PROFESSIONAL CORPORATION</small></div>
<div class="abs top-contact">Free Consultation<br>
  <svg width="13" height="13" viewBox="0 0 24 24"><path fill="#ab9566" d="M6.6 10.8a15 15 0 0 0 6.6 6.6l2.2-2.2c.3-.3.7-.4 1-.2 1.1.4 2.3.6 3.6.6.6 0 1 .4 1 1V20c0 .6-.4 1-1 1A17 17 0 0 1 3 4c0-.6.4-1 1-1h3.5c.6 0 1 .4 1 1 0 1.3.2 2.5.6 3.6.1.3 0 .7-.2 1z"/></svg> (555) 014-2278<br>
  <span class="lang">English &#8964;</span></div>
<nav class="abs nav">
  <div class="nav-mark"><span></span></div>
  <ul><li>HOME</li><li>DORIAN KESSLY</li><li>PRACTICE AREAS</li><li>INSIGHTS</li><li>CONTACT</li></ul>
</nav>
<div class="abs hero-name">Dorian Kessly Law</div>

<section class="abs intro">
  <h1 class="abs h-serif">Criminal and <b>Civil Trial</b> Lawyer</h1>
  <p class="abs">Dorian Kessly law is a lawfirm serving the Sacramento ipsum dolor sit amet, consectetur adipiscing elit, sed do eiusmod tempor incididunt ut labore et dolore magna aliqua. Ut enim ad minim veniam, quis nostrud exercitation ullamco laboris nisi ut aliquip ex ea commodo consequat.</p>
  <div class="abs card c1" role="img" aria-label="Photo of handcuffed hands">Criminal Defense</div>
  <div class="abs card c2" role="img" aria-label="Photo of a handshake over documents">Civil Litigation</div>
  <div class="abs card c3" role="img" aria-label="Photo of the Statue of Liberty">Immigration</div>
  <div class="abs card c4" role="img" aria-label="Photo of two women reviewing papers">Family Law</div>
</section>

<section class="abs about">
  <h2 class="abs h-serif">Ready, <b>Reliable</b> and<br>Expereinced</h2>
  <p class="abs">Lorem ipsum dolor sit amet, consectetur adipiscing elit, sed do eiusmod tempor incididunt ut labore et dolore magna aliqua. Nibh tellus molestie nunc non. Risus nec feugiat in fermentum posuere urna nec tincidunt praesent. Felis imperdiet proin fermentum leo vel orci porta non. Vitae semper quis lectus nulla at. Sagittis orci a scelerisque purus. Id nibh tortor id aliquet lectus proin. Ac turpis egestas maecenas pharetra convallis posuere morbi leo urna.</p>
  <div class="abs btn-outline">ABOUT DORIAN</div>
  <div class="abs portrait" role="img" aria-label="Headshot of the attorney in a dark suit and grey tie"></div>
</section>

<section class="abs consult">
  <h3 class="abs">Schedule A Free Consultation</h3>
  <div class="abs field" style="top:143px">First Name</div>
  <div class="abs field" style="top:191px">Email</div>
  <div class="abs field" style="top:239px">Phone Number</div>
  <div class="abs field" style="top:288px;height:78px">Please enter a breif description of you case</div>
  <div class="abs submit">SUBMIT</div>
  <h2 class="abs h-serif">When you contact Dorian Kessly law for a free consulting..</h2>
  <p class="abs">Lorem ipsum dolor sit amet, consectetur adipiscing elit, sed do eiusmod tempor incididunt ut labore et dolore magna aliqua. Nibh tellus molestie nunc non. Risus nec feugiat in fermentum posuere urna nec tincidunt praesent. Felis imperdiet proin fermentum leo vel orci porta non.</p>
</section>

<footer class="abs footer">
  <div class="abs foot-brand">DORIAN KESSLY LAW<small>A PROFESSIONAL CORPORATION</small></div>
  <div class="abs foot-col" style="left:417px"><h4>Contact Info</h4>2718 Larkspur Row<br>Suite # 305<br>Fairhaven, CA 95731</div>
  <div class="abs foot-col" style="left:667px"><h4>Quick Links</h4>Home<br>Dorian Kessly<br>Practice Areas<br>Insights<br>Contact<br>Privacy Policy</div>
  <div class="abs foot-col" style="left:894px"><h4>Follow Us</h4>
    <div class="social" aria-label="Social links"><span></span><span></span><span></span></div></div>
</footer>
<div class="abs legal">
  <p>Lorem ipsum dolor sit amet, consectetur adipiscing elit, sed do eiusmod tempor incididunt ut labore et dolore magna aliqua. Nibh tellus molestie nunc non. Risus nec feugiat in fermentum posuere urna nec tincidunt praesent. Felis imperdiet proin fermentum leo vel orci porta non. Vitae semper quis lectus nulla at.</p>
  <small>2021 Dorian Kessly. All rights reserved.</small>
</div>

</body>
</html>
```